Woman owned consulting company needs an elegant and modern business card design

I need a business card design for my new consulting company, Mira Holcombe Consulting. I am looking for something that is simple and elegant, but also creative and original. You can use either version of the logo that are attached. I have also included the information that needs to be featured on the business card.

Contact Information for Business Card

Requirements
Must have
• The logo and the font type and a standard business card size. Use shades of gray/silver and or rose gold that are in the logo.
• I didn't realize that my actual logo wasn't attached. Please incorporate in the designs.
Should not have
• Colors that are different from my logo

```html
<!DOCTYPE html>
<html lang="en">
<head>
<meta charset="utf-8">
<title>Mira Holcombe Consulting – Business Cards</title>
<link href="https://fonts.googleapis.com/css2?family=Open+Sans:wght@400;600;700&display=swap" rel="stylesheet">
<style>
  :root {
    --charcoal: #414143;
    --silver: #d3d3d6;
    --paper: #ffffff;
    --stage: #ecebe8;
    --ink: #2b2b2d;
    --ink-soft: #555558;
  }
  * { box-sizing: border-box; margin: 0; padding: 0; }
  html, body {
    width: 1200px; height: 900px; overflow: hidden;
    background: var(--stage);
    font-family: "Open Sans", Arial, sans-serif;
  }
  .card {
    position: absolute;
    width: 520px; height: 297px;
    box-shadow: 0 10px 28px rgba(0,0,0,.18);
    overflow: hidden;
  }
  .card svg.shapes { position: absolute; inset: 0; }
  .card-front { left: 50px; top: 302px; background: var(--paper); }
  .card-back { left: 630px; top: 302px; background: var(--charcoal); }

  /* front */
  .owner { position: absolute; left: 150px; top: 16px; color: var(--ink); }
  .owner-name { font-size: 22px; font-weight: 700; letter-spacing: .5px; line-height: 1; }
  .owner-title { font-size: 10px; font-weight: 600; letter-spacing: .5px; margin-top: 2px; }
  .contact-list { position: absolute; left: 22px; top: 116px; list-style: none; color: var(--ink); }
  .contact-list li { display: flex; align-items: center; gap: 9px; font-size: 15px; line-height: 24px; }
  .contact-list svg { width: 11px; height: 11px; flex: none; }
  .front-brand {
    position: absolute; left: 280px; top: 218px; width: 170px;
    text-align: center;
    font-size: 17px; font-weight: 600; color: var(--charcoal); line-height: 1.2;
  }

  /* back */
  .back-brand {
    position: absolute; left: 60px; top: 118px; width: 190px;
    font-size: 19px; font-weight: 600; color: var(--silver); line-height: 1.25;
  }
  .divider { position: absolute; left: 262px; top: 92px; width: 2px; height: 118px; background: var(--paper); }
  .services { position: absolute; left: 278px; top: 100px; list-style: none; color: var(--paper); }
  .services li { font-size: 13.5px; line-height: 20px; }
  .services li::before { content: "· "; }
  .back-web { position: absolute; left: 24px; top: 246px; font-size: 15px; color: var(--paper); letter-spacing: .3px; }
</style>
</head>
<body>

<section class="card card-front" aria-label="Card front">
  <svg class="shapes" viewBox="0 0 520 297" aria-hidden="true">
    <path d="M0 0 H210 L150 22 Q128 30 136 52 L140 62 L0 118 Z" fill="var(--charcoal)"/>
    <path d="M0 118 L140 62 Q120 72 112 52 L104 30 Q98 14 118 8 L150 0" fill="none" stroke="var(--silver)" stroke-width="4"/>
    <path d="M150 297 L380 162 Q404 148 418 172 L496 297 Z" fill="var(--silver)" stroke="var(--ink)" stroke-width="4"/>
  </svg>

  <div class="owner">
    <p class="owner-name">MIRA HOLCOMBE</p>
    <p class="owner-title">OWNER</p>
  </div>

  <ul class="contact-list">
    <li>
      <svg viewBox="0 0 12 12" aria-hidden="true"><rect x="3" y="0.5" width="6" height="11" rx="1" fill="none" stroke="var(--ink)"/><circle cx="6" cy="9.5" r=".8" fill="var(--ink)"/></svg>
      (555)-214-7730
    </li>
    <li>
      <svg viewBox="0 0 12 12" aria-hidden="true"><rect x="0.5" y="2.5" width="11" height="7" fill="var(--ink)"/><path d="M0.5 2.5 L6 7 L11.5 2.5" fill="none" stroke="var(--paper)"/></svg>
      mira@miraholcombeconsulting.com
    </li>
    <li>
      <svg viewBox="0 0 12 12" aria-hidden="true"><circle cx="6" cy="6" r="5.5" fill="var(--ink-soft)"/><path d="M0.5 6 H11.5 M6 0.5 V11.5" stroke="var(--paper)" stroke-width=".8"/></svg>
      www.miraholcombeconsulting.com
    </li>
  </ul>

  <p class="front-brand">Mira Holcombe<br>Consulting</p>
</section>

<section class="card card-back" aria-label="Card back">
  <svg class="shapes" viewBox="0 0 520 297" aria-hidden="true">
    <path d="M0 0 H250 L120 46 Q98 54 94 32 L88 0 Z M0 0 H88 L94 32 Q98 54 76 60 L0 82 Z" fill="var(--silver)"/>
    <path d="M250 -2 L120 46 Q98 54 94 32 L88 -2 M0 82 L76 60 Q98 54 94 32" fill="none" stroke="var(--paper)" stroke-width="4"/>
    <path d="M520 297 H270 L400 251 Q422 243 426 265 L432 297 Z M520 297 H432 L426 265 Q422 243 444 237 L520 215 Z" fill="var(--silver)"/>
    <path d="M270 299 L400 251 Q422 243 426 265 L432 299 M520 215 L444 237 Q422 243 426 265" fill="none" stroke="var(--paper)" stroke-width="4"/>
  </svg>

  <p class="back-brand">Mira Holcombe Consulting</p>
  <div class="divider"></div>
  <ul class="services">
    <li>Business Consultant</li>
    <li>Business Coaching Specialist</li>
    <li>Independent Contractor</li>
    <li>Event Production Specialist</li>
    <li>Event Consultant</li>
  </ul>
  <p class="back-web">www.miraholcombeconsulting.com</p>
</section>

</body>
</html>
```